Velvet & Vine by Mona
Text 410.582.3174 to set up and appointment
Instagram is Velvet_VineByMona
Location 4182 Carrow Ln. Notthingham Md, 21094 Suit 204
Slogan "Polished Looks. Radiant Days.
Specializing in pressicion cuts, blonding, fades, perms, waxing and more

The salon is black, gun metal color mirror with led lights. Green plants and has natural wood countertops for accent colors. Modern yet elegant. I want the card simple but it needs something to really grab the clients attention. I like black, grey, gold, green, natural tones and hints of pink or gold coloring
I’m open to anything. I don’t have a logo. Suggestions are welcome

Target Market(s)

20-60 men and woman

Industry/Entity Type

Hairstylist / barber

The name of the show should be bold. Maybe the letters could raised I also like foil for shine added or a mat finish

Colors

Requirements
Must have
• I also like some floral Floral designs, but not too overpowering. I like Sparkle, Watercolor design, Or a geometric line in the background
Nice to have
• I’m really here because I need creative help. I’m open for suggestions. I’ll post a picture of the salon in inspiration if I can find it.
Should not have
• Checkered background

```html
<!DOCTYPE html>
<html lang="en">
<head>
<meta charset="utf-8">
<title>Velvet &amp; Vine by Mona — Business Card</title>
<link rel="stylesheet" href="https://fonts.googleapis.com/css2?family=Outfit:wght@300;400;600&family=Mrs+Saint+Delafield&display=swap">
<style>
  :root {
    --backdrop: #b4b4b4;
    --card-dark: #474747;
    --card-light: #f1f1f0;
    --ink: #2e2e2e;
    --ink-soft: #4a4a4a;
    --gold: #c9a961;
    --tagline-light: #e4e4e4;
  }
  * { margin: 0; padding: 0; box-sizing: border-box; }
  html, body {
    width: 1200px; height: 900px; overflow: hidden;
    background: var(--backdrop);
    font-family: "Outfit", sans-serif;
  }
  .canvas { position: relative; width: 1200px; height: 900px; }

  .card { position: absolute; left: 393px; width: 414px; height: 236px; }
  .card--front { top: 196px; background: var(--card-dark); }
  .card--back  { top: 492px; background: var(--card-light); color: var(--ink); }

  /* Front */
  .brand-name {
    position: absolute; left: 0; right: 0; top: 100px;
    text-align: center; color: var(--gold);
    font-weight: 300; font-size: 22px; line-height: 1; letter-spacing: 0.3px;
    white-space: nowrap;
  }
  .front-tagline {
    position: absolute; left: 0; right: 0; top: 200px;
    text-align: center; color: var(--tagline-light);
    font-size: 6.5px; letter-spacing: 2.2px; font-weight: 400;
  }

  /* Back */
  .services {
    position: absolute; left: 44px; top: 40px;
    border-left: 1px solid var(--ink);
    padding-left: 7px; font-size: 7.5px; line-height: 9.5px; color: var(--ink-soft);
  }
  .script-tagline {
    position: absolute; left: 46px; top: 72px;
    font-family: "Mrs Saint Delafield", cursive;
    font-size: 15px; line-height: 1; color: var(--ink-soft); white-space: nowrap;
  }
  .person { position: absolute; right: 43px; top: 38px; text-align: right; }
  .person__name { font-size: 18px; line-height: 1; color: var(--ink); font-weight: 400; white-space: nowrap; }
  .person__name strong { font-weight: 600; }
  .person__role { font-size: 7px; color: var(--ink-soft); margin-top: 2px; }

  .contact {
    position: absolute; left: 44px; top: 161px;
    font-size: 7.5px; line-height: 11px; color: var(--ink-soft);
    list-style: none; white-space: nowrap;
  }
  .contact li { display: flex; align-items: center; gap: 4px; }
  .contact strong { font-weight: 600; color: var(--ink); }
  .contact__icon { width: 7px; height: 7px; flex: none; }
  .contact__dot {
    width: 6px; height: 6px; border-radius: 50%;
    border: 1px solid var(--ink-soft); flex: none; margin-right: 1px;
  }

  .brand-mini {
    position: absolute; right: 43px; top: 172px;
    color: var(--gold); font-weight: 300; font-size: 10px; line-height: 1;
    white-space: nowrap;
  }
</style>
</head>
<body>
<main class="canvas">
  <section class="card card--front" aria-label="Card front">
    <p class="brand-name">Velvet &amp; Vine by Mona</p>
    <p class="front-tagline">POLISHED LOOKS &nbsp;•&nbsp; RADIANT DAYS</p>
  </section>

  <section class="card card--back" aria-label="Card back">
    <div class="services">
      <p>Pressicion cuts</p>
      <p>Blonding, Fades</p>
      <p>Perms, Waxing &amp; more</p>
    </div>
    <p class="script-tagline">polished looks . radiant days</p>

    <div class="person">
      <p class="person__name"><strong>Mona</strong> Kessler</p>
      <p class="person__role">Managing Director</p>
    </div>

    <ul class="contact">
      <li>4182 Carrow Ln. Notthingham Md, 21094 Suit 204</li>
      <li>
        <svg class="contact__icon" viewBox="0 0 10 10" aria-hidden="true">
          <path d="M1 1.5h8v5.5H4L2 8.8V7H1z" fill="none" stroke="#4a4a4a" stroke-width="1"/>
          <path d="M2.6 3.4h4.8M2.6 5h3.4" stroke="#4a4a4a" stroke-width="0.8"/>
        </svg>
        <span><strong>410.582.3174</strong> - Text to book an appointment</span>
      </li>
      <li><span class="contact__dot"></span>Velvet_VineByMona</li>
    </ul>

    <p class="brand-mini">Velvet &amp; Vine by Mona</p>
  </section>
</main>
</body>
</html>
```